Broschüre für Konzepte rund um Immobilien
Zielgruppe
Wir sind ein junges, dynamisches Team und unterstützen Kunden mit individuellen, abgestimmten Konzepten rund um Ihre Immobilie - daher suchen wir ein hochwertiges Design, unsere Zielgruppe liegt Wert auf was neues, nicht das was jeder hat.
Aufgabenstellung
Die Farben und das Layout sollen von der Homepage übernommen werden www.k7-zelt.de..
Den Text entnehmen Sie der angehängten Datei. Bilder, Anordnungen und sonstiges überlasse ich Ihren kreativen Geist! DIN A5 Querformat - Bilder und Texte müssen in einer sehr hohen Auflösung umsetzbar sein!

```html
<!DOCTYPE html>
<html lang="de">
<head>
<meta charset="utf-8">
<title>K7ZELT – Broschüre Immobilienkonzepte</title>
<link rel="stylesheet" href="https://fonts.googleapis.com/css2?family=Archivo+Narrow:wght@600;700&family=Libre+Franklin:wght@400;500;600&display=swap">
<style>
  :root {
    --backdrop: #464646;
    --paper: #ffffff;
    --navy: #16213a;
    --ink: #111111;
    --muted: #7d7d7d;
  }
  * { margin: 0; padding: 0; box-sizing: border-box; }
  html, body { width: 1200px; height: 2477px; overflow: hidden; background: var(--backdrop); }
  .canvas { position: relative; width: 1200px; height: 2477px; font-family: "Libre Franklin", Arial, sans-serif; color: var(--ink); }
  .page { position: absolute; background: var(--paper); overflow: hidden; }
  .photo { position: absolute; }

  .cover { left: 333px; top: 0; width: 556px; height: 314px; }
  .cover .photo {
    inset: 0;
    background:
      radial-gradient(ellipse 60% 45% at 30% 85%, rgba(70,70,70,.85) 0%, rgba(70,70,70,0) 100%),
      radial-gradient(ellipse 45% 35% at 80% 20%, rgba(235,235,235,.9) 0%, rgba(235,235,235,0) 100%),
      linear-gradient(180deg, #9a9a9a 0%, #c4c4c4 35%, #7c7c7c 65%, #585858 100%);
  }
  .cover-title { position: absolute; left: 52px; top: 6px; font-family: "Archivo Narrow", "Arial Narrow", sans-serif; font-weight: 700; font-size: 31px; line-height: 40px; color: var(--navy); }
  .brand-box { position: absolute; left: 305px; top: 157px; width: 201px; height: 118px; background: var(--navy); display: flex; align-items: center; justify-content: center; gap: 10px; }
  .brand-box .dot { width: 12px; height: 12px; border-radius: 50%; background: #e8e8e8; }
  .brand-box .name { font-family: "Libre Franklin", Arial, sans-serif; font-weight: 400; font-size: 20px; letter-spacing: 2px; color: #e8e8e8; }

  .spread { left: 55px; width: 1115px; height: 391px; }
  .copy { position: absolute; font-size: 7px; line-height: 10px; font-weight: 600; }
  .copy p + p { margin-top: 7px; }
  .copy .lead { color: var(--muted); }
  .heading { position: absolute; text-align: right; font-family: "Archivo Narrow", "Arial Narrow", sans-serif; font-weight: 700; font-size: 7.5px; line-height: 9px; }
  .heading small { display: block; font-family: "Libre Franklin", Arial, sans-serif; font-weight: 400; font-size: 5.5px; line-height: 7px; color: var(--muted); }

  .closing { left: 333px; top: 2400px; width: 556px; height: 77px; }
</style>
</head>
<body>
<div class="canvas">

  <section class="page cover">
    <div class="photo" role="img" aria-label="Wohnraum mit grauem Sofa vor großer Fensterfront, schwarz-weiß"></div>
    <h1 class="cover-title">Wir planen und<br>gestalten Ihren<br>persönlichen<br>LEBENS[T]RAUM</h1>
    <div class="brand-box"><span class="dot"></span><span class="name">K7ZELT</span></div>
  </section>

  <section class="page spread" style="top:336px">
    <div class="photo" role="img" aria-label="Dunkles Loft-Wohnzimmer mit grauem Ecksofa und Küchenzeile" style="left:0;top:0;width:683px;height:391px;background:
      radial-gradient(ellipse 22% 18% at 12% 38%, rgba(214,196,160,.85) 0%, rgba(214,196,160,0) 100%),
      radial-gradient(ellipse 18% 35% at 50% 22%, rgba(190,192,190,.7) 0%, rgba(190,192,190,0) 100%),
      radial-gradient(ellipse 12% 30% at 94% 25%, rgba(205,210,205,.75) 0%, rgba(205,210,205,0) 100%),
      radial-gradient(ellipse 45% 30% at 40% 72%, rgba(120,118,116,.8) 0%, rgba(120,118,116,0) 100%),
      linear-gradient(180deg, #3a3a3c 0%, #2b2a29 55%, #1e1d1c 100%)"></div>
    <div class="copy" style="left:764px;top:150px;width:293px">
      <p>Ein Zuhause, das zu Ihnen passt: Wir begleiten Sie von der ersten Idee bis zur fertigen Umsetzung und verbinden Ihre Wünsche mit durchdachter Planung, hochwertigen Materialien und einem klaren Blick für Details.</p>
      <p>Jedes Konzept entsteht individuell und im engen Austausch mit Ihnen, damit am Ende Räume entstehen, die begeistern.</p>
      <p>Ob Neubau, Sanierung oder Modernisierung – wir denken Ihre Immobilie ganzheitlich und schaffen Werte, die bleiben.</p>
    </div>
  </section>

  <section class="page spread" style="top:749px">
    <div class="heading" style="left:90px;top:136px;width:100px">Konzept &amp; Planung<small>Leistung</small></div>
    <div class="copy" style="left:206px;top:150px;width:296px">
      <p>Wir analysieren Ihre Räume, Ihre Abläufe und Ihre Vorstellungen. Daraus entwickeln wir ein stimmiges Gesamtkonzept mit Grundriss, Materialauswahl und Lichtplanung, abgestimmt auf Budget und Zeitrahmen.</p>
      <p class="lead">Alles aus einer Hand geplant.</p>
      <p>Von der Küche bis zum Wohnbereich koordinieren wir alle Gewerke zuverlässig und termingerecht für Sie.</p>
    </div>
    <div class="photo" role="img" aria-label="Küche mit dunklen Fliesen, Holzboden und Esstisch" style="left:608px;top:38px;width:454px;height:317px;background:
      radial-gradient(ellipse 40% 20% at 75% 88%, rgba(150,150,145,.7) 0%, rgba(150,150,145,0) 100%),
      linear-gradient(180deg, #cfc8bb 0%, #bfb7a8 18%, #3a3b3a 24%, #2c2d2c 48%, #5b4636 58%, #8d6a47 72%, #9c7750 100%)"></div>
  </section>

  <section class="page spread" style="top:1161px">
    <div class="photo" role="img" aria-label="Treppe mit Holzstufen von oben gesehen" style="left:52px;top:39px;width:182px;height:220px;background:
      radial-gradient(ellipse 50% 30% at 55% 80%, rgba(190,140,90,.9) 0%, rgba(190,140,90,0) 100%),
      linear-gradient(165deg, #ececea 0%, #bdb8b0 25%, #5a4c40 50%, #2a2624 70%, #a57b52 100%)"></div>
    <div class="photo" role="img" aria-label="Sechseckige Bodenfliesen in Holzoptik" style="left:242px;top:176px;width:264px;height:179px;background:
      radial-gradient(ellipse 35% 40% at 60% 45%, rgba(200,178,150,.75) 0%, rgba(200,178,150,0) 100%),
      linear-gradient(135deg, #3e2c20 0%, #6e513b 40%, #8c6d52 60%, #3a2a20 100%)"></div>
    <div class="heading" style="left:604px;top:135px;width:150px">Böden, Treppen &amp; Oberflächen<small>Material</small></div>
    <div class="copy" style="left:764px;top:150px;width:298px">
      <p>Holz, Fliesen und Naturstein verleihen jedem Raum Charakter. Wir beraten Sie zu Formaten, Verlegemustern und Pflege und setzen Ihre Auswahl mit erfahrenen Partnern präzise um – langlebig und stilsicher.</p>
    </div>
  </section>

  <section class="page spread" style="top:1574px">
    <div class="heading" style="left:89px;top:138px;width:108px">Bad &amp; Wellness<small>Komfort</small></div>
    <div class="copy" style="left:206px;top:152px;width:296px">
      <p>Ihr Badezimmer wird zum privaten Rückzugsort. Wir planen Duschen, Wannen und Armaturen funktional und elegant und achten auf clevere Stauraumlösungen sowie angenehme Beleuchtung.</p>
    </div>
    <div class="photo" role="img" aria-label="Moderne Dusche mit schwarzer Armatur" style="left:608px;top:77px;width:146px;height:185px;background:
      radial-gradient(ellipse 30% 40% at 25% 60%, rgba(230,230,228,.85) 0%, rgba(230,230,228,0) 100%),
      linear-gradient(90deg, #2a2c2d 0%, #6d7070 30%, #3b3d3e 60%, #1f2122 100%)"></div>
    <div class="photo" role="img" aria-label="Badezimmer mit freistehender Wanne und gemusterten Fliesen" style="left:762px;top:118px;width:300px;height:198px;background:
      radial-gradient(ellipse 22% 14% at 38% 72%, rgba(240,238,232,.95) 0%, rgba(240,238,232,0) 100%),
      radial-gradient(ellipse 14% 40% at 88% 40%, rgba(235,232,225,.8) 0%, rgba(235,232,225,0) 100%),
      linear-gradient(180deg, #c9c1b4 0%, #b3aa9c 30%, #3f3b39 42%, #4a4442 62%, #4e382b 78%, #3a2a21 100%)"></div>
  </section>

  <section class="page spread" style="top:1987px">
    <div class="heading" style="left:118px;top:84px;width:109px">Wohnen &amp; Einrichten<small>Stil</small></div>
    <div class="copy" style="left:233px;top:104px;width:150px">
      <p>Mit passenden Möbeln, Farben und Textilien entsteht eine Atmosphäre, in der Sie sich vom ersten Tag an wohlfühlen. Wir stimmen jedes Detail auf Ihren Stil ab.</p>
    </div>
    <div class="heading" style="left:24px;top:220px;width:110px">Service &amp; Betreuung<small>Begleitung</small></div>
    <div class="copy" style="left:142px;top:234px;width:145px">
      <p>Auch nach der Übergabe sind wir für Sie da – mit Wartung, Anpassungen und einem offenen Ohr für neue Ideen rund um Ihre Immobilie.</p>
    </div>
    <div class="photo" role="img" aria-label="Helles Wohnzimmer mit weißem Sofa, Kissen und Pflanzen" style="left:432px;top:0;width:683px;height:391px;background:
      radial-gradient(ellipse 30% 30% at 60% 22%, rgba(250,250,250,1) 0%, rgba(250,250,250,0) 100%),
      radial-gradient(ellipse 30% 25% at 32% 78%, rgba(236,236,234,.95) 0%, rgba(236,236,234,0) 100%),
      radial-gradient(ellipse 25% 20% at 55% 80%, rgba(90,90,92,.6) 0%, rgba(90,90,92,0) 100%),
      radial-gradient(ellipse 25% 25% at 82% 85%, rgba(160,125,90,.7) 0%, rgba(160,125,90,0) 100%),
      linear-gradient(180deg, #e4e4e2 0%, #d2d2d0 55%, #a49c92 100%)"></div>
  </section>

  <section class="page closing">
    <div class="photo" role="img" aria-label="Raumausschnitt in Grautönen" style="left:432px;top:0;width:124px;height:77px;background:linear-gradient(135deg,#7a7a7a 0%,#4e4e4e 100%)"></div>
  </section>

</div>
</body>
</html>
```